Business Card Re-Design/Update

We'd like to update out business cards. I've included our current "Style guide" which has the colour scheme of the organisation in it. I've also included the branding files with logos etc in them.

I've also included a copy of one of our existing cards so that you can see how ugly/dated they look. I'd like a fresh modern corporate look.

Target Market(s)

These are for our clients, potential clients, industry contacts - like all business cards

Contact Information for Business Card

Name
Position
Company Address - Level 1, 52 Copperfield Road, Dunmore Qld 4071
Direct Phone
mobile
Email
Website -www.korvelit.com.au
Logo

Colors

Designer to choose colors to be used in the design.

Requirements
Must have
• Main Logo
• Cards will need to be editable to be able to personalize them for each new employee.
Nice to have
• The MapIT, HandIT, KeepIT would be okay to have if they can be sensibly and professionally added to the look without detracting from the main imagery.
• Maybe they could go on the back of the card? will leave this to your creative discretion as to whether/where they fit.
Should not have
• Should not have decorative or script fonts

```html
<!DOCTYPE html>
<html lang="en">
<head>
<meta charset="utf-8">
<title>korvelIT business card</title>
<link rel="stylesheet" href="https://fonts.googleapis.com/css2?family=Roboto:wght@300;400;500;700&family=Roboto+Condensed:wght@400;700&display=swap">
<style>
  :root {
    --page-bg: #e9e9ea;
    --card-white: #fbfbfb;
    --brand-red: #d71920;
    --brand-red-deep: #a80f16;
    --ink: #2a2a2a;
    --ink-soft: #5a5a5a;
    --faint-red: rgba(215, 25, 32, 0.08);
  }
  * { box-sizing: border-box; margin: 0; padding: 0; }
  html, body { width: 1200px; height: 911px; overflow: hidden; }
  body {
    background: var(--page-bg);
    font-family: "Roboto", Arial, sans-serif;
    display: flex;
    align-items: center;
    justify-content: center;
    gap: 40px;
  }
  .card {
    position: relative;
    width: 540px;
    height: 310px;
    overflow: hidden;
    box-shadow: 0 10px 28px rgba(0,0,0,0.18);
  }

  /* Front */
  .card--front { background: var(--card-white); }
  .front__watermark {
    position: absolute;
    left: -40px; bottom: -70px;
    width: 260px; height: 260px;
    background: var(--faint-red);
  }
  .brand {
    position: absolute;
    top: 70px; left: 230px;
    display: flex; align-items: center; gap: 12px;
  }
  .brand__square {
    width: 34px; height: 34px;
    background: var(--brand-red);
  }
  .brand__name {
    font-family: "Roboto", Arial, sans-serif;
    font-weight: 500;
    font-size: 40px;
    letter-spacing: -1px;
    color: var(--ink);
  }
  .person {
    position: absolute;
    left: 34px; bottom: 108px;
    padding-left: 12px;
    border-left: 5px solid var(--brand-red);
  }
  .person__name {
    font-family: "Roboto Condensed", Arial, sans-serif;
    font-weight: 700;
    font-size: 20px;
    color: var(--brand-red);
    text-transform: uppercase;
    line-height: 1.1;
  }
  .person__title {
    font-family: "Roboto Condensed", Arial, sans-serif;
    font-size: 14px;
    color: var(--ink);
  }
  .contacts {
    position: absolute;
    left: 51px; bottom: 20px;
    list-style: none;
    font-size: 13px;
    color: var(--ink-soft);
    line-height: 17px;
  }
  .contacts li { display: flex; align-items: center; gap: 8px; }
  .contacts svg { width: 11px; height: 11px; flex: none; }
  .address {
    position: absolute;
    right: 28px; bottom: 24px;
    text-align: right;
    font-size: 13px;
    font-weight: 300;
    color: var(--ink-soft);
    line-height: 18px;
    font-style: normal;
  }

  /* Back */
  .card--back {
    background: linear-gradient(135deg, var(--brand-red) 0%, #c8141b 50%, var(--brand-red-deep) 100%);
  }
  .back__watermark {
    position: absolute;
    left: 40px; top: -40px;
    width: 220px; height: 220px;
    background: rgba(0,0,0,0.08);
    transform: rotate(0deg);
  }
  .taglines {
    position: absolute;
    right: 44px; bottom: 34px;
    list-style: none;
    color: #fff;
    font-weight: 700;
    font-size: 40px;
    line-height: 42px;
    letter-spacing: -0.5px;
  }
</style>
</head>
<body>
  <section class="card card--front" aria-label="Business card front">
    <div class="front__watermark"></div>
    <div class="brand">
      <span class="brand__square"></span>
      <span class="brand__name">korvelIT</span>
    </div>
    <div class="person">
      <p class="person__name">Dana Whitlock</p>
      <p class="person__title">Business Development Manager</p>
    </div>
    <ul class="contacts">
      <li><svg viewBox="0 0 12 12"><path d="M2 1h3l1 3-2 1a7 7 0 0 0 3 3l1-2 3 1v3c-6 0-9-3-9-9z" fill="var(--brand-red)"/></svg>+61 (0)7 3148 2207</li>
      <li><svg viewBox="0 0 12 12"><path d="M2 1h3l1 3-2 1a7 7 0 0 0 3 3l1-2 3 1v3c-6 0-9-3-9-9z" fill="var(--brand-red)"/></svg>+61 (0)7 3148 2215</li>
      <li><svg viewBox="0 0 12 12"><rect x="3" y="0.5" width="6" height="11" rx="1" fill="none" stroke="var(--brand-red)" stroke-width="1.4"/></svg>+61 (0)431 560 284</li>
      <li><svg viewBox="0 0 12 12"><rect x="1" y="4" width="10" height="6" fill="var(--brand-red)"/><rect x="3" y="1" width="6" height="3" fill="none" stroke="var(--brand-red)"/></svg>+61 (0)7 3148 2290</li>
      <li><svg viewBox="0 0 12 12"><rect x="0.5" y="2" width="11" height="8" fill="var(--brand-red)"/><path d="M1 2.5l5 4 5-4" fill="none" stroke="#fff" stroke-width="1"/></svg>dwhitlock@korvelit.com.au</li>
    </ul>
    <address class="address">
      Level 1, 52 Copperfield Road<br>
      Dunmore Qld 4071<br>
      www.korvelit.com.au
    </address>
  </section>

  <section class="card card--back" aria-label="Business card back">
    <div class="back__watermark"></div>
    <ul class="taglines">
      <li>MapIT</li>
      <li>HandIT</li>
      <li>KeepIT</li>
    </ul>
  </section>
</body>
</html>
```